Clockharbour Homepage Banner 1060 W x 100 H

Please see the attached 'word' document (Also copied below)
Feel free to use any images or logos from our website.
www.clockharbour.com.au

Background:
We are an Australian based official watch distributor/online retailer of international watch brands.

We require a new banner ad (1060 W x 100 H) to replace the existing one on our homepage www.clockharbour.com.au & wish to convey the following information:
*(Please feel free to alter wording, include or exclude points below & generally take creative license (with commercial reality in mind). We sell some luxury watches, so it must look professional & maintain a luxury look & feel.)

Clockharbour Direct:
Revolutionising the retail watch market !

- Buy direct from the official distributor & get world competitive
online prices (with full international warranty, & all original
papers, box & invoice)

- Eliminate all risk of fakes & non-existent factory warranty from
'grey' market sellers

- Free worldwide delivery over A$300

- Order online & 'try-on' in the comfort of your own home.
If you're not 100% happy, just post it back for a full refund or
exchange within 30 days

- Prefer to see & try on before purchase? Visit one of our retail
partner stores.

*** Feel free to copy any images from our website
www.clockharbour.com.au
Updates

Target Market(s)

Luxury watches

Industry/Entity Type

Retail

Font styles to use
Sans Serif

Requirements
Must have
• Visual imagery, text
Nice to have
• Feel free to use your creativity...
Should not have
• Cheap looking or tacky images. We sell some luxury watches, so we need to keep a professional & luxury image.

```html
<!DOCTYPE html>
<html lang="en">
<head>
<meta charset="utf-8">
<title>Clockharbour Direct Banner</title>
<link rel="stylesheet" href="https://fonts.googleapis.com/css2?family=Archivo+Narrow:wght@700&family=Roboto+Condensed:wght@700&display=swap">
<style>
  :root {
    --bg: #000000;
    --bg-edge: #0d0d0d;
    --gold: #c5a46d;
    --white: #ffffff;
    --watch-dark: #3a2418;
    --watch-mid: #8a5a3a;
    --watch-light: #c9a27a;
  }
  html, body {
    margin: 0;
    padding: 0;
    width: 1200px;
    height: 113px;
    overflow: hidden;
    background: var(--bg);
  }
  .banner {
    position: relative;
    width: 1200px;
    height: 113px;
    background: linear-gradient(90deg, var(--bg) 0%, var(--bg) 70%, var(--bg-edge) 100%);
    overflow: hidden;
  }
  .banner__headline {
    position: absolute;
    left: 32px;
    top: 36px;
    margin: 0;
    font-family: "Archivo Narrow", "Roboto Condensed", sans-serif;
    font-weight: 700;
    font-size: 38px;
    line-height: 40px;
    letter-spacing: 0.5px;
    color: var(--gold);
  }
  .banner__offer {
    position: absolute;
    left: 283px;
    top: 26px;
    margin: 0;
    font-family: "Roboto Condensed", "Archivo Narrow", sans-serif;
    font-weight: 700;
    font-size: 25px;
    line-height: 32px;
    color: var(--white);
  }
  .banner__watch {
    position: absolute;
    left: 900px;
    top: -30px;
    width: 300px;
    height: 180px;
    border-radius: 50%;
    background: radial-gradient(ellipse at 45% 55%, var(--watch-light) 0%, var(--watch-mid) 40%, var(--watch-dark) 65%, var(--bg) 80%);
  }
</style>
</head>
<body>
  <div class="banner">
    <h1 class="banner__headline">BUY DIRECT</h1>
    <p class="banner__offer">The Official Distributor &amp;<br>Get World Competitive Online Prices</p>
    <div class="banner__watch" role="img" aria-label="Luxury rose gold skeleton watch with visible movement"></div>
  </div>
</body>
</html>
```